Nanotechnology meets nature cosmetic company needs label design. Name of the company is QuillaBloom

We are a cosmetic brand that combines nanotechnology with nature in the form of hemp extracts and essential oils, creating products that provide pain relief as well as stress reduction and relaxation. We have three different products and need three separate labels. We have a logo and would like to incorporate that into the label design. The colors are teal, black and gray. We would like to convey a message of combining nature with cutting edge cosmetic technology.
1. Topical pain lotion
2. Bath soak
3. Massage lotion
The logo is attached and I would just like the logo used and not the text below. The colors of the logo should be teal cross and "V" inside the gray lines that make up the circle with black color inside the circle. If this can't be done, I can send another logo.

```html
<!DOCTYPE html>
<html lang="en">
<head>
<meta charset="UTF-8">
<title>QuillaBloom Topical Pain Lotion Label</title>
<link href="https://fonts.googleapis.com/css2?family=Poppins:wght@300;400;600;700&display=swap" rel="stylesheet">
<style>
  :root {
    --teal: #1fb8a5;
    --teal-band: #22c2ad;
    --label-black: #161616;
    --label-gray: #3a3a3a;
    --white: #ffffff;
    --copy-gray: #e8e8e8;
    --backdrop: #f2f2f2;
    --divider: #444444;
  }
  html, body {
    margin: 0;
    padding: 0;
    width: 1083px;
    height: 1200px;
    overflow: hidden;
    background: var(--backdrop);
    font-family: "Poppins", sans-serif;
  }
  .label {
    position: absolute;
    left: 311px;
    top: 28px;
    width: 460px;
    height: 1143px;
    background: linear-gradient(100deg, var(--label-black) 0%, #1e1e1e 45%, var(--label-gray) 75%, var(--label-black) 100%);
    overflow: hidden;
  }
  .brand {
    position: absolute;
    top: 180px;
    left: 0;
    width: 100%;
    display: flex;
    align-items: center;
    justify-content: center;
    gap: 14px;
  }
  .brand-dot {
    width: 26px;
    height: 26px;
    border-radius: 50%;
    background: var(--teal);
  }
  .brand-name {
    font-weight: 600;
    font-size: 44px;
    color: var(--teal);
    line-height: 1;
  }
  .headline {
    position: absolute;
    left: 12px;
    margin: 0;
    font-weight: 600;
    line-height: 1;
    white-space: nowrap;
    letter-spacing: -6px;
  }
  .headline-topical { top: 340px; font-size: 112px; color: var(--teal); }
  .headline-pain { top: 452px; font-size: 124px; color: var(--white); }
  .headline-lotion { top: 570px; font-size: 120px; color: var(--white); }
  .subtitle {
    position: absolute;
    top: 708px;
    left: 14px;
    margin: 0;
    font-weight: 300;
    font-size: 27px;
    color: var(--copy-gray);
    white-space: nowrap;
    letter-spacing: -0.5px;
  }
  .nature-copy {
    position: absolute;
    top: 778px;
    left: 14px;
    margin: 0;
    font-weight: 300;
    font-size: 23px;
    line-height: 30px;
    color: var(--teal);
  }
  .anatomy-art {
    position: absolute;
    left: 185px;
    top: 760px;
    width: 260px;
    height: 300px;
    border-radius: 40% 30% 40% 30%;
    background: radial-gradient(ellipse at 50% 45%, #2d7fb8 0%, #1a4f7a 40%, rgba(22,22,22,0) 75%);
  }
  .benefits {
    position: absolute;
    top: 940px;
    left: 14px;
    margin: 0;
    padding: 0;
    list-style: none;
    width: 160px;
  }
  .benefits li {
    font-weight: 600;
    font-size: 19px;
    color: var(--white);
    height: 37px;
    line-height: 34px;
    border-bottom: 1px solid var(--divider);
    white-space: nowrap;
  }
  .benefits li:last-child { border-bottom: none; }
  .benefits li::before {
    content: "•";
    font-size: 14px;
    margin-right: 4px;
  }
  .net-band {
    position: absolute;
    left: 0;
    bottom: 0;
    width: 100%;
    height: 72px;
    background: var(--teal-band);
    display: flex;
    align-items: center;
  }
  .net-weight {
    margin-left: 14px;
    font-weight: 300;
    font-size: 27px;
    color: var(--white);
  }
</style>
</head>
<body>
  <section class="label">
    <div class="brand">
      <span class="brand-dot"></span>
      <span class="brand-name">QuillaBloom</span>
    </div>

    <h1 class="headline headline-topical">TOPICAL</h1>
    <h1 class="headline headline-pain">PAIN</h1>
    <h1 class="headline headline-lotion">LOTION</h1>

    <p class="subtitle">Stress Reduction and Relaxation</p>

    <p class="nature-copy">With nature<br>in the form of<br>hemp extracts<br>&amp; essential oils</p>

    <div class="anatomy-art" role="img" aria-label="Illustration of a running human figure in blue x-ray style with highlighted red joints"></div>

    <ul class="benefits">
      <li>Fast Acting</li>
      <li>Non-Greasy</li>
      <li>No Burning</li>
    </ul>

    <div class="net-band">
      <span class="net-weight">Net wt. 4oz. (113.4g)</span>
    </div>
  </section>
</body>
</html>
```